Red Gum Business Card Design

We are a new small business specialising in under ground cable jointing and excavation works in NSW Australia.
Design I'm looking for is incorporating the Australian flag & excavator with out being to cheesy.
Maybe a faded washed out flag to help with overload of colour? & so its not the main focus.
Very open to creative out of the box designs!

Target Market(s)

Building & Construction

Industry/Entity Type

Construction

Contact Information for Business Card

Red Gum Cable Jointing & Excavations
Owen Falkirk

Ph: 0438 605 312
E: owen.falkirk@tallmail.example

Reverse Side
Services we offer:
High Voltage & Low Voltage Cable Jointing
Polymeric & paperlead jointing & terminations
Trenching & Auger Drilling 150 - 600mm
Site preparation / leveling / clearing
Driveway / Footpath / Turf Prep
Rubbish Removal
Tree & Stump removal
Footings & Post holes
Drainage
Service Installs
Gravels & Sands available
Any general Earth moving needs
Reliable Free Quotes
Fully Insured

Font styles to use
Serif
Script

Requirements
Nice to have
• small excavator (See uploaded picture)

```html
<!DOCTYPE html>
<html lang="en">
<head>
<meta charset="utf-8">
<title>Red Gum Business Card Design</title>
<link href="https://fonts.googleapis.com/css2?family=Lato:wght@400;700&display=swap" rel="stylesheet">
<style>
  :root {
    --page-bg: #2b2b2d;
    --wash-deep: #1d4fbf;
    --wash-mid: #2f6fd9;
    --wash-light: #6aa6f2;
    --flag-red: #e8415c;
    --flag-white: #f4f4f8;
    --ink-navy: #10245a;
    --name-tint: #bcd6fb;
    --star: #ffffff;
    --kangaroo: #b68654;
    --excavator: #d7b43a;
  }
  html, body {
    margin: 0;
    width: 1200px;
    height: 997px;
    overflow: hidden;
    background: var(--page-bg);
    font-family: "Lato", sans-serif;
  }
  .stage {
    position: relative;
    width: 1200px;
    height: 997px;
  }
  .card {
    position: absolute;
    width: 700px;
    height: 400px;
    overflow: hidden;
    background:
      radial-gradient(circle at 30% 70%, var(--wash-light) 0%, transparent 45%),
      radial-gradient(circle at 80% 20%, var(--wash-light) 0%, transparent 40%),
      linear-gradient(135deg, var(--wash-mid), var(--wash-deep));
    box-shadow: 0 12px 30px rgba(0,0,0,.5);
  }
  .card--back { left: 80px; top: 60px; }
  .card--front { left: 420px; top: 520px; }
  .card__art {
    position: absolute;
    inset: 0;
    width: 700px;
    height: 400px;
  }
  .illustration {
    position: absolute;
    border-radius: 40% 50% 45% 40%;
  }
  .illustration--kangaroo {
    left: 300px; top: 40px; width: 330px; height: 230px;
    background: radial-gradient(ellipse at 45% 55%, var(--kangaroo) 0%, rgba(182,134,84,.55) 45%, transparent 72%);
  }
  .illustration--excavator {
    left: 470px; top: 100px; width: 220px; height: 190px;
    background: radial-gradient(ellipse at 55% 50%, var(--excavator) 0%, rgba(60,60,60,.6) 50%, transparent 74%);
  }
  .details {
    position: absolute;
    left: 48px;
    top: 212px;
    color: var(--ink-navy);
  }
  .details__company {
    margin: 0 0 14px;
    font-size: 22px;
    font-weight: 400;
  }
  .details__name {
    margin: 0 0 22px;
    font-size: 22px;
    font-weight: 400;
    letter-spacing: 1px;
    color: var(--name-tint);
    text-transform: uppercase;
  }
  .contact {
    list-style: none;
    margin: 0;
    padding: 0;
    font-size: 19px;
  }
  .contact__item {
    display: flex;
    align-items: center;
    gap: 14px;
    margin-bottom: 14px;
  }
  .contact__icon { width: 16px; height: 16px; flex: none; }
</style>
</head>
<body>
<main class="stage">

  <svg width="0" height="0" style="position:absolute">
    <defs>
      <symbol id="federation-star" viewBox="-10 -10 20 20">
        <polygon fill="var(--star)" points="0,-10 1.95,-4.05 7.82,-6.23 4.39,-1 9.75,2.23 3.52,2.81 4.34,9.01 0,4.5 -4.34,9.01 -3.52,2.81 -9.75,2.23 -4.39,-1 -7.82,-6.23 -1.95,-4.05"/>
      </symbol>
      <clipPath id="jack-clip"><rect width="60" height="30"/></clipPath>
      <clipPath id="jack-diag">
        <path d="M30,15 h30 v15 z v15 h-30 z h-30 v-15 z v-15 h30 z"/>
      </clipPath>
      <symbol id="union-jack" viewBox="0 0 60 30">
        <g clip-path="url(#jack-clip)" opacity=".85">
          <rect width="60" height="30" fill="var(--wash-mid)" opacity="0"/>
          <path d="M0,0 L60,30 M60,0 L0,30" stroke="var(--flag-white)" stroke-width="6"/>
          <path d="M0,0 L60,30 M60,0 L0,30" clip-path="url(#jack-diag)" stroke="var(--flag-red)" stroke-width="4"/>
          <path d="M30,0 v30 M0,15 h60" stroke="var(--flag-white)" stroke-width="10"/>
          <path d="M30,0 v30 M0,15 h60" stroke="var(--flag-red)" stroke-width="6"/>
        </g>
      </symbol>
    </defs>
  </svg>

  <section class="card card--back" aria-label="Card reverse">
    <svg class="card__art" viewBox="0 0 700 400">
      <use href="#union-jack" x="-20" y="110" width="340" height="170"/>
      <use href="#federation-star" x="150" y="290" width="70" height="70"/>
      <use href="#federation-star" x="480" y="25" width="40" height="40"/>
      <use href="#federation-star" x="580" y="140" width="38" height="38"/>
      <use href="#federation-star" x="370" y="45" width="30" height="30"/>
      <use href="#federation-star" x="640" y="250" width="26" height="26"/>
    </svg>
    <div class="illustration illustration--kangaroo" role="img" aria-label="Watercolour kangaroo holding an Australian flag"></div>
  </section>

  <section class="card card--front" aria-label="Card front">
    <svg class="card__art" viewBox="0 0 700 400">
      <use href="#union-jack" x="0" y="0" width="230" height="115"/>
      <use href="#federation-star" x="95" y="130" width="60" height="60"/>
      <use href="#federation-star" x="300" y="30" width="34" height="34"/>
      <use href="#federation-star" x="420" y="20" width="30" height="30"/>
      <use href="#federation-star" x="250" y="95" width="28" height="28"/>
      <use href="#federation-star" x="380" y="110" width="32" height="32"/>
      <use href="#federation-star" x="530" y="40" width="30" height="30"/>
      <use href="#federation-star" x="630" y="20" width="28" height="28"/>
      <use href="#federation-star" x="600" y="80" width="24" height="24"/>
      <use href="#federation-star" x="560" y="300" width="40" height="40"/>
      <use href="#federation-star" x="650" y="130" width="26" height="26"/>
    </svg>
    <div class="illustration illustration--excavator" role="img" aria-label="Photo of a small yellow excavator"></div>
    <div class="details">
      <h1 class="details__company">Red Gum Cable Jointing &amp; Excavations</h1>
      <p class="details__name">Owen Falkirk</p>
      <ul class="contact">
        <li class="contact__item">
          <svg class="contact__icon" viewBox="0 0 16 16"><rect x="4" y="1" width="8" height="14" rx="1.5" fill="none" stroke="var(--flag-white)" stroke-width="1.5"/></svg>
          <span>0438 605 312</span>
        </li>
        <li class="contact__item">
          <svg class="contact__icon" viewBox="0 0 16 16"><rect x="1" y="3" width="14" height="10" fill="none" stroke="var(--flag-white)" stroke-width="1.3"/><path d="M1,3 L8,9 L15,3" fill="none" stroke="var(--flag-white)" stroke-width="1.3"/></svg>
          <span>owen.falkirk@tallmail.example</span>
        </li>
      </ul>
    </div>
  </section>

</main>
</body>
</html>
```